Business Card Design Project

Professional business cards for law firm - a rough example of what we are looking for is attached. The logo, colour and styling of the name are all new and dont need to be changed. We need layout for front and back. We are looking for some imaginative layout of info. We are a young vibrant firm and not too conservative and are not adverse to something quite different.
Updates

Thank you for all the submissions.  We have been blown away with the quality of your work.  Our management team will be meeting later in the week to make our decision.  Again, thanks for the fabulous work.

Industry/Entity Type

Conservative

Requirements
Must have
• Logo and name as in attached example (colour and font)
Should not have
• Scales of Justice

```html
<!DOCTYPE html>
<html lang="en">
<head>
<meta charset="utf-8">
<title>Harper Lane Legal – Business Cards</title>
<link rel="stylesheet" href="https://fonts.googleapis.com/css2?family=Open+Sans:wght@400;700&family=Arimo:wght@400&display=swap">
<style>
  :root {
    --slate: #5b7089;
    --slate-mid: #aab6c4;
    --paper: #ffffff;
    --olive: #5f7a2f;
    --navy: #1d3250;
    --stage: #ffffff;
  }
  * { box-sizing: border-box; margin: 0; padding: 0; }
  html, body { width: 1200px; height: 1200px; overflow: hidden; background: var(--stage); }
  .canvas { position: relative; width: 1200px; height: 1200px; }

  .card {
    position: absolute;
    left: 220px;
    width: 760px;
    height: 460px;
    box-shadow: 0 4px 14px rgba(0,0,0,0.25);
    overflow: hidden;
  }
  .card--front { top: 90px; background: linear-gradient(90deg, var(--slate) 0%, var(--slate-mid) 45%, var(--paper) 88%); }
  .card--back  { top: 650px; background: linear-gradient(90deg, var(--paper) 4%, var(--slate-mid) 50%, var(--slate) 100%); }

  .wordmark {
    position: absolute;
    font-family: "Open Sans", sans-serif;
    font-weight: 700;
    color: var(--olive);
    text-align: center;
    line-height: 1;
  }
  .wordmark__name { display: block; font-size: 38px; letter-spacing: -0.3px; }
  .wordmark__sub  { display: block; font-size: 21px; letter-spacing: 3px; margin-top: 6px; font-weight: 700; }

  .card--front .brand-circle {
    position: absolute;
    left: 305px; top: 185px;
    width: 112px; height: 112px;
    border: 3px solid var(--navy);
    border-radius: 50%;
  }
  .card--front .wordmark { left: 450px; top: 200px; }

  .services {
    position: absolute;
    right: 38px; top: 330px;
    font-family: "Arimo", sans-serif;
    font-size: 15px;
    color: var(--navy);
    line-height: 1.55;
    text-align: right;
  }

  .card--back .wordmark { left: 45px; top: 150px; }
  .divider {
    position: absolute;
    left: 300px; top: 70px;
    width: 3px; height: 200px;
    background: var(--olive);
  }
  .contact {
    position: absolute;
    left: 335px; top: 110px;
    font-family: "Open Sans", sans-serif;
    font-size: 18px;
    line-height: 1.45;
    color: var(--navy);
    font-style: normal;
  }
  .contact .email { margin-top: 6px; display: block; }
</style>
</head>
<body>
<main class="canvas">
  <section class="card card--front" aria-label="Card front">
    <span class="brand-circle" aria-hidden="true"></span>
    <div class="wordmark">
      <span class="wordmark__name">Harper Lane</span>
      <span class="wordmark__sub">LEGAL</span>
    </div>
    <p class="services">
      Family &nbsp;.&nbsp; Restraining Orders &nbsp;.&nbsp; Probate/wills &nbsp;.&nbsp; Dividing Fences<br>
      Traffic &nbsp;.&nbsp; Criminal &nbsp;.&nbsp; Debt Recovery &nbsp;.&nbsp; Financial Agreements
    </p>
  </section>

  <section class="card card--back" aria-label="Card back">
    <div class="wordmark">
      <span class="wordmark__name">Harper Lane</span>
      <span class="wordmark__sub">LEGAL</span>
    </div>
    <span class="divider" aria-hidden="true"></span>
    <address class="contact">
      7/52 Carrow Street, Ridgeford WA 6120<br>
      PO Box 312, Ridgeford WA 6981<br>
      T: 9321 4570 . 6210 3388<br>
      F: 6402 1195
      <span class="email">reception@harperlanelegal.com.au</span>
    </address>
  </section>
</main>
</body>
</html>
```